Smoked and Dried Fish Business Cards

We need a business card design for a new company called The Harbour Reed Limited. We import smoked and dried fish from Ghana and distribute worldwide. We would like to see designs that use colours red yellow and green. The final design should communicate healthy and saftey food environment.

Industry/Entity Type

Business

Contact Information for Business Card

The Harbour Reed Limited.
87 Moreton Rise. Larchfield Vale.
London.
SE14 3QB.
TEL: 01482 739215. Mobile. 07861 302957 /07725190846
Website: www.harbourreedltd.com email: sales@harbourreedltd.com

```html
<!DOCTYPE html>
<html lang="en">
<head>
<meta charset="utf-8">
<title>The Harbour Reed Limited – Business Card</title>
<link rel="stylesheet" href="https://fonts.googleapis.com/css2?family=Berkshire+Swash&family=Cabin+Condensed:wght@500&display=swap">
<style>
  :root {
    --card-green: #a2cf55;
    --skyline-green: #8fbf45;
    --accent-red: #c8282d;
    --accent-yellow: #f6c928;
    --accent-green: #2f8a3c;
    --ink-white: #ffffff;
    --ink-dark: #141a0a;
  }
  html, body {
    margin: 0;
    padding: 0;
    width: 1200px;
    height: 791px;
    overflow: hidden;
    background: var(--card-green);
  }
  .card {
    position: relative;
    width: 1200px;
    height: 791px;
    background: var(--card-green);
    overflow: hidden;
    font-family: "Cabin Condensed", "Arial Narrow", sans-serif;
  }
  .skyline-art {
    position: absolute;
    left: 0;
    top: 150px;
    width: 1200px;
    height: 560px;
  }
  .brand-mark {
    position: absolute;
    left: 550px;
    top: 124px;
    width: 112px;
    height: 112px;
    border-radius: 50%;
    background: var(--accent-yellow);
  }
  .company-name {
    position: absolute;
    left: 0;
    top: 280px;
    width: 1200px;
    margin: 0;
    text-align: center;
    font-family: "Berkshire Swash", cursive;
    font-weight: 400;
    font-size: 53px;
    line-height: 1;
    color: var(--ink-white);
  }
  .address {
    position: absolute;
    left: 0;
    top: 372px;
    width: 1200px;
    margin: 0;
    text-align: center;
    font-size: 27px;
    word-spacing: 5px;
    color: var(--ink-dark);
  }
  .contact {
    position: absolute;
    top: 548px;
    margin: 0;
    font-size: 29px;
    line-height: 45px;
    color: var(--ink-white);
    word-spacing: 3px;
  }
  .contact-phones { left: 90px; }
  .contact-online { left: 735px; }
  .contact p { margin: 0; }
  .colour-band {
    position: absolute;
    left: 0;
    bottom: 0;
    width: 1200px;
    height: 14px;
    display: flex;
  }
  .colour-band span { flex: 1; }
  .band-red { background: var(--accent-red); }
  .band-yellow { background: var(--accent-yellow); }
  .band-green { background: var(--accent-green); }
</style>
</head>
<body>
  <div class="card">
    <svg class="skyline-art" viewBox="0 0 1200 560" role="img" aria-label="Faint London skyline with observation wheel, Tower Bridge and Parliament">
      <defs>
        <radialGradient id="skyline-glow" cx="50%" cy="55%" r="60%">
          <stop offset="0%" stop-color="#8fbf45" stop-opacity="0.55"/>
          <stop offset="100%" stop-color="#8fbf45" stop-opacity="0"/>
        </radialGradient>
      </defs>
      <rect x="0" y="0" width="1200" height="560" fill="url(#skyline-glow)"/>
    </svg>

    <div class="brand-mark"></div>
    <h1 class="company-name">The Harbour Reed Limited</h1>
    <p class="address">87 Moreton Rise. Larchfield Vale. London. SE14 3QB.</p>

    <div class="contact contact-phones">
      <p>TEL: 01482 739215</p>
      <p>Mb. 07861 302957 / 07725190846</p>
    </div>
    <div class="contact contact-online">
      <p>Website: www.harbourreedltd.com</p>
      <p>Email: sales@harbourreedltd.com</p>
    </div>

    <div class="colour-band">
      <span class="band-red"></span>
      <span class="band-yellow"></span>
      <span class="band-green"></span>
    </div>
  </div>
</body>
</html>
```